Name card design for KOV mobile accessories company

KOV is an upmarket brand, we are looking for professional business card design.

the design should be neat and simple but giving a strong feeling.
should not be colorful. make it black/white/gray tone

Name:
Job title:
Contact no.:
company address: i would like the company address to be very small and thin.
link to social media profile:
company website:

*the company have no website yet
as the project is done please i also would like the font that use in design as well; for more further people in company need a business card:)
Updates

Thank you for all super fast submission :D they're all look cool!

i have just update my brief to make the statement clearer, please check it out :)
if you have any question please dont hesitate to ask.
i would like see more design from you! 
Keep it up!  :D

Target Market(s)

Company target are upmarket company distributor, such as Vordane and Pilto store.

Industry/Entity Type

Business

Font styles to use
Serif
Sans Serif
Other font styles liked:
• Formal and mordern

Colors
ffffff
eeeeee
d3d3d3
919191
474747
1b1b1b
000000
333333

Requirements
Must have
• The design must be professional clean and clear but also Strong and Modern!
text should be formal and mordern
Should not have
• No complicated design!

```html
<!DOCTYPE html>
<html lang="en">
<head>
<meta charset="utf-8">
<title>KOV Business Card</title>
<link rel="stylesheet" href="https://fonts.googleapis.com/css2?family=Roboto:wght@300;400;700;900&display=swap">
<style>
  :root {
    --stage: #1b1b1b;
    --card-light: #ffffff;
    --card-dark: #333333;
    --ink: #1b1b1b;
    --ink-soft: #474747;
    --ink-muted: #919191;
    --rule: #d3d3d3;
    --white: #ffffff;
  }
  * { margin: 0; padding: 0; box-sizing: border-box; }
  html, body {
    width: 1200px; height: 638px; overflow: hidden;
    background: var(--stage);
    font-family: "Roboto", Arial, sans-serif;
  }
  .stage {
    position: relative; width: 1200px; height: 638px;
    display: flex; align-items: center; justify-content: center; gap: 60px;
  }
  .card {
    position: relative; width: 500px; height: 286px;
  }
  .card-front { background: var(--card-light); color: var(--ink); }
  .card-back {
    background: var(--card-dark); color: var(--white);
    display: flex; align-items: center; justify-content: center;
  }
  .holder { position: absolute; left: 40px; top: 44px; }
  .holder-name { font-size: 14px; font-weight: 700; letter-spacing: 0.5px; text-transform: uppercase; }
  .holder-title { font-size: 11px; font-weight: 300; font-style: italic; color: var(--ink-soft); margin-top: 2px; }
  .contact-list {
    list-style: none; margin-top: 12px; padding-left: 10px;
    border-left: 1px solid var(--rule);
  }
  .contact-item {
    display: flex; align-items: center; gap: 6px;
    font-size: 11px; font-weight: 400; color: var(--ink-soft); line-height: 16px;
  }
  .contact-icon { width: 9px; height: 9px; fill: none; stroke: var(--ink-soft); stroke-width: 1.4; }
  .address {
    margin-top: 10px; font-size: 10.5px; font-weight: 300; color: var(--ink-soft);
  }
  .brand-mark {
    position: absolute; right: 40px; top: 44px;
    font-size: 54px; font-weight: 900; letter-spacing: 2px; color: var(--ink-soft); line-height: 1;
  }
  .social-list {
    position: absolute; right: 40px; bottom: 36px;
    display: flex; gap: 8px; list-style: none;
    font-size: 8px; font-weight: 400; color: var(--ink-muted);
  }
  .brand-mark-large {
    font-size: 150px; font-weight: 900; letter-spacing: 8px; color: var(--white); line-height: 1;
  }
</style>
</head>
<body>
<main class="stage">
  <section class="card card-front" aria-label="Business card front">
    <div class="holder">
      <p class="holder-name">Dara Lenn</p>
      <p class="holder-title">President</p>
      <ul class="contact-list">
        <li class="contact-item">
          <svg class="contact-icon" viewBox="0 0 10 10"><path d="M2 1h2l1 2.5-1.3 1a5 5 0 0 0 2 2l1-1.3L9 6v2a1 1 0 0 1-1 1A7 7 0 0 1 1 2a1 1 0 0 1 1-1z"/></svg>
          480.555.0141
        </li>
        <li class="contact-item">
          <svg class="contact-icon" viewBox="0 0 10 10"><rect x="2.5" y="1" width="5" height="8" rx="1"/><path d="M4.5 7.5h1"/></svg>
          602.555.0120
        </li>
        <li class="contact-item">
          <svg class="contact-icon" viewBox="0 0 10 10"><rect x="1" y="2" width="8" height="6"/><path d="M1 2l4 3.5L9 2"/></svg>
          info@kovgear.com
        </li>
        <li class="contact-item">
          <svg class="contact-icon" viewBox="0 0 10 10"><circle cx="5" cy="5" r="4"/><path d="M1 5h8M5 1c-2 2.5-2 5.5 0 8M5 1c2 2.5 2 5.5 0 8"/></svg>
          www.kovgear.com
        </li>
      </ul>
      <p class="address">18 B Harlow Street, Denton TX 7620</p>
    </div>
    <p class="brand-mark">KOV</p>
    <ul class="social-list" aria-label="Social profiles">
      <li>Circlr</li>
      <li>Chirpy</li>
      <li>Facenet</li>
      <li>Linkwise</li>
    </ul>
  </section>

  <section class="card card-back" aria-label="Business card back">
    <p class="brand-mark-large">KOV</p>
  </section>
</main>
</body>
</html>
```